8 1/2 x 8 1/2 Social Media Design Ad - Commercial Loan Originator

Wanted
Commercial Loan Originators

* No Licensing Required
* Lend Nationwide with few exceptions
* Competitive Compensation
* You find the Investors and we handle the rest!!!

PRODUCTS
* Debt Service Coverage Loans (DSCR)
* Fix & Flip Financing
* Ground Up Construction
* Bridge Loans
* Portfolio Loans
And many more.....

Call (800) 417-9265 x24 for more information

Brightmoor Lending Partners, Inc.
7200 Warbleton Avenue, Harwick Falls, MD 21587
NMLS #318640

```html
<!DOCTYPE html>
<html lang="en">
<head>
<meta charset="utf-8">
<title>Wanted – Commercial Loan Originators</title>
<link href="https://fonts.googleapis.com/css2?family=Tinos:wght@700&family=Poppins:wght@400;600;700&family=Oswald:wght@600&display=swap" rel="stylesheet">
<style>
  :root{
    --gold-light:#f9c85c;
    --gold:#c8922f;
    --gold-dark:#9c5f12;
    --blue:#1d49b8;
    --blue-bright:#2d6fe0;
    --navy:#0b1f5e;
    --navy-deep:#0a1a52;
    --white:#ffffff;
    --ink:#0d1f5c;
  }
  *{box-sizing:border-box;margin:0;padding:0}
  html,body{width:1200px;height:1200px;overflow:hidden;background:var(--white)}
  .ad{position:relative;width:1200px;height:1200px;background:var(--white);overflow:hidden;font-family:"Poppins",sans-serif}
  .top-band{position:absolute;left:0;top:0;width:1200px;height:189px;
    background:linear-gradient(90deg,#dca646 0%,var(--gold-light) 18%,#d9a343 40%,var(--gold-dark) 62%,#a2651a 100%)}
  .blue-band{position:absolute;left:0;top:196px;width:1200px;height:82px;
    background:linear-gradient(90deg,var(--blue) 0%,var(--blue-bright) 45%,var(--blue) 100%)}
  .brand-disc{position:absolute;left:44px;top:44px;width:438px;height:438px;border-radius:50%;background:var(--white)}
  .brand{position:absolute;left:44px;top:150px;width:438px;text-align:center;color:var(--navy)}
  .brand-dot{width:58px;height:58px;border-radius:50%;background:var(--gold);margin:0 auto 16px}
  .brand-name{font-weight:700;font-size:30px;line-height:1.15}
  .headline{position:absolute;left:466px;top:34px;width:700px;font-family:"Tinos",serif;font-weight:700;
    font-size:152px;line-height:1;color:var(--white);letter-spacing:4px}
  .subhead{position:absolute;left:503px;top:196px;height:82px;line-height:82px;font-weight:700;font-size:42px;color:var(--white)}
  .features{position:absolute;left:54px;top:343px}
  .feature{position:absolute;left:0;width:546px;height:112px}
  .feature-line{position:absolute;left:0;top:0}
  .feature-icon{position:absolute;left:0;top:0;width:112px;height:112px;border-radius:50%;border:3px solid var(--gold);background:var(--white)}
  .feature-icon svg{position:absolute;left:9px;top:9px}
  .feature-text{position:absolute;left:137px;top:14px;font-weight:700;font-size:32px;line-height:40px;color:var(--ink)}
  .products-title{position:absolute;left:54px;top:864px;font-family:"Tinos",serif;font-weight:700;font-size:47px;color:var(--gold);letter-spacing:1px}
  .products-frame{position:absolute;left:0;top:0}
  .product-list{position:absolute;left:54px;top:944px;list-style:none}
  .product-list li{display:flex;align-items:center;height:35.5px;font-size:28.5px;color:var(--ink)}
  .product-list svg{margin-right:12px;flex:none}
  .product-more{color:var(--gold);font-weight:700;margin-left:8px}
  .photo{position:absolute;left:657px;top:360px;width:504px;height:560px;border:2px solid var(--navy);border-bottom:none;
    border-radius:36px 36px 0 0;background:linear-gradient(160deg,#bcd9ef 0%,#7fb0dc 35%,#3f6fae 70%,#c9d6e6 100%)}
  .contact{position:absolute;left:657px;top:902px;width:504px;height:248px;border-radius:18px 18px 26px 26px;overflow:hidden}
  .contact-call{height:45px;background:var(--blue);display:flex;align-items:center;justify-content:center;gap:14px;
    font-family:"Tinos",serif;font-weight:700;font-size:26px;color:var(--white);letter-spacing:.5px}
  .contact-call .rule{width:72px;height:2px;background:var(--gold)}
  .contact-phone{height:102px;background:var(--navy-deep);text-align:center;color:var(--white)}
  .phone-number{font-family:"Oswald",sans-serif;font-weight:600;font-size:55px;line-height:74px;letter-spacing:0}
  .phone-note{font-family:"Tinos",serif;font-size:21px;letter-spacing:3px;line-height:20px}
  .contact-address{height:101px;background:var(--gold);text-align:center;color:var(--white);font-weight:600;font-size:18.5px;line-height:27px;padding-top:10px}
  .contact-address .nmls{font-weight:700}
  .bottom-band{position:absolute;left:12px;top:1186px;width:1176px;height:40px;border-radius:24px 24px 0 0;
    background:linear-gradient(90deg,var(--gold-dark) 0%,#c98a2c 40%,var(--gold-light) 70%,#e2ae4c 100%)}
</style>
</head>
<body>
<div class="ad">
  <div class="top-band"></div>
  <div class="blue-band"></div>
  <div class="brand-disc"></div>
  <div class="brand">
    <div class="brand-dot"></div>
    <div class="brand-name">Brightmoor Lending<br>Partners, Inc.</div>
  </div>
  <h1 class="headline">WANTED</h1>
  <div class="subhead">Commercial Loan Originators</div>

  <div class="features">
    <svg class="feature-line" width="560" height="540" viewBox="0 0 560 540" fill="none" stroke="#c8922f" stroke-width="2">
      <path d="M56 110 H533 a12 12 0 0 0 12 -12 V22"/><circle cx="545" cy="22" r="4" fill="#c8922f"/>
      <path d="M56 236 H533 a12 12 0 0 0 12 -12 V134"/><circle cx="545" cy="134" r="4" fill="#c8922f"/>
      <path d="M56 362 H533 a12 12 0 0 0 12 -12 V250"/><circle cx="545" cy="250" r="4" fill="#c8922f"/>
      <path d="M56 488 H533 a12 12 0 0 0 12 -12 V365"/><circle cx="545" cy="365" r="4" fill="#c8922f"/>
    </svg>

    <div class="feature" style="top:0">
      <div class="feature-icon"><svg width="88" height="88" viewBox="0 0 88 88"><circle cx="44" cy="44" r="44" fill="#1333a0"/><circle cx="44" cy="44" r="26" fill="none" stroke="#fff" stroke-width="4"/><rect x="35" y="30" width="18" height="24" fill="none" stroke="#fff" stroke-width="3"/><line x1="26" y1="62" x2="62" y2="26" stroke="#fff" stroke-width="4"/></svg></div>
      <div class="feature-text">No Licensing<br>Required</div>
    </div>
    <div class="feature" style="top:126px">
      <div class="feature-icon"><svg width="88" height="88" viewBox="0 0 88 88"><circle cx="44" cy="44" r="44" fill="#1333a0"/><circle cx="44" cy="36" r="12" fill="#fff"/><text x="44" y="41" text-anchor="middle" font-size="14" font-weight="700" fill="#1333a0" font-family="Poppins,sans-serif">$</text><path d="M22 58 q10 -6 22 0 h12 l10 -6" fill="none" stroke="#fff" stroke-width="4" stroke-linecap="round"/></svg></div>
      <div class="feature-text">Lend Nationwide<br>with few exceptions</div>
    </div>
    <div class="feature" style="top:252px">
      <div class="feature-icon"><svg width="88" height="88" viewBox="0 0 88 88"><circle cx="44" cy="44" r="44" fill="#1333a0"/><path d="M44 22 c12 6 16 14 14 22 h-28 c-2 -8 2 -16 14 -22z" fill="#fff"/><text x="44" y="42" text-anchor="middle" font-size="14" font-weight="700" fill="#1333a0" font-family="Poppins,sans-serif">$</text><path d="M24 58 h16 l8 4 h14 l8 -6" fill="none" stroke="#fff" stroke-width="4" stroke-linecap="round"/></svg></div>
      <div class="feature-text">Competitive<br>Compensation</div>
    </div>
    <div class="feature" style="top:378px">
      <div class="feature-icon"><svg width="88" height="88" viewBox="0 0 88 88"><circle cx="44" cy="44" r="44" fill="#1333a0"/><circle cx="36" cy="30" r="9" fill="#fff"/><path d="M20 62 v-10 a14 14 0 0 1 28 0 v10z" fill="#fff"/><circle cx="58" cy="52" r="12" fill="none" stroke="#fff" stroke-width="3"/><text x="58" y="57" text-anchor="middle" font-size="13" font-weight="700" fill="#fff" font-family="Poppins,sans-serif">$</text></svg></div>
      <div class="feature-text">You find the Investors<br>and we handle the rest</div>
    </div>
  </div>

  <svg class="products-frame" width="1200" height="1200" viewBox="0 0 1200 1200" fill="none" stroke="#c8922f" stroke-width="1.5">
    <path d="M341 902 H626 a15 15 0 0 1 15 15 V1135 a15 15 0 0 1 -15 15 H38"/>
  </svg>
  <div class="products-title">PRODUCTS</div>
  <ul class="product-list">
    <li><svg width="20" height="20" viewBox="0 0 20 20"><circle cx="10" cy="10" r="8" fill="none" stroke="#1d49b8" stroke-width="2"/><path d="M5 10 l4 4 l8 -10" fill="none" stroke="#1d49b8" stroke-width="2.5"/></svg>Debt Service Coverage Loans (DSCR)</li>
    <li><svg width="20" height="20" viewBox="0 0 20 20"><circle cx="10" cy="10" r="8" fill="none" stroke="#1d49b8" stroke-width="2"/><path d="M5 10 l4 4 l8 -10" fill="none" stroke="#1d49b8" stroke-width="2.5"/></svg>Fix &amp; Flip Financing</li>
    <li><svg width="20" height="20" viewBox="0 0 20 20"><circle cx="10" cy="10" r="8" fill="none" stroke="#1d49b8" stroke-width="2"/><path d="M5 10 l4 4 l8 -10" fill="none" stroke="#1d49b8" stroke-width="2.5"/></svg>Ground Up Construction</li>
    <li><svg width="20" height="20" viewBox="0 0 20 20"><circle cx="10" cy="10" r="8" fill="none" stroke="#1d49b8" stroke-width="2"/><path d="M5 10 l4 4 l8 -10" fill="none" stroke="#1d49b8" stroke-width="2.5"/></svg>Bridge Loans</li>
    <li><svg width="20" height="20" viewBox="0 0 20 20"><circle cx="10" cy="10" r="8" fill="none" stroke="#1d49b8" stroke-width="2"/><path d="M5 10 l4 4 l8 -10" fill="none" stroke="#1d49b8" stroke-width="2.5"/></svg>Portfolio Loans<span class="product-more">And many more.....</span></li>
  </ul>

  <div class="photo" role="img" aria-label="Photo of a loan originator in shirt and tie reviewing a tablet at an office desk by bright windows"></div>

  <div class="contact">
    <div class="contact-call"><span class="rule"></span>CALL US TODAY AT<span class="rule"></span></div>
    <div class="contact-phone">
      <div class="phone-number">(800) 417-9265 X24</div>
      <div class="phone-note">For More Information</div>
    </div>
    <div class="contact-address">
      Brightmoor Lending Partners, Inc.<br>
      7200 Warbleton Avenue, Harwick Falls, MD 21587<br>
      <span class="nmls">NMLS #318640</span>
    </div>
  </div>

  <div class="bottom-band"></div>
</div>
</body>
</html>
```